Lumoveri.com Postcard Design

Lumoveri.com LLC began in January 2014 after a 3-year development. Our website is https://lumoveri.example. We need a two-side postcard design [oversized, 8.52" x 5.47"] to introduce upper-income American Moms with at least one child 4-9 to two different Lumoveri products simultaneously -- Lumoveri: Steady Steps To Balance, and Lumoveri: Little Pages Adventure. There is much information on the website about both products, and free demos of everything. Design should include the following copy:

Quiet Hurts -- Healed.

You can't seem to stick with your nutrition and activity plans.

Tears from your little one (4 and up), who is too fast, or too slow, for the school's reading program.

Forgive yourself. For less than $10 a month*, Science can help you with either or both of these quiet hurts.

https://lumoveri.example

*(annual subscription)

[Edit] With much thanks to designs already submitted, to clarify:

We want to sell HEALING, not hurt, SOLUTIONS, not problems! Empowering, optimistic, even joyful, is what we want to convey.

Which is to say, "You've just discovered that Help is on the way!" These are two difficult real-life problems OVER WHICH A MOM CAN HAVE MUCH MORE CONTROL THAN SHE PREVIOUSLY THOUGHT.

These two real problems must be mentioned up front (NOT apart from the rest of the text -- WHAT problems can be healed is what we are selling), AND must be 'swaddled' in optimism, encouragement, and empowerment. Unicorns and bunnies, super-mom! -- whatever, we're not graphic designers. But NOT an ad for an anti-depressant!

Oops! Originally forgot to indicate that an oversize postcard is needed: dimensions 8.52" x 5.47". Brief has been edited to include this information.

Target Market(s)

Again, we'd like to interest upper-income American Moms with at least one child 4-9

Industry/Entity Type

Nutrition

Requirements
Nice to have
• You're welcome to squeeze a picture of Gus in somewhere, with copy similar to the site at lumoveri.example:
Buy Gus! And Pals At Brindlemart
Read all the stories in Lumoveri: Little Pages Adventure for just 99 cents!
But that's just because Gus's so cute. Up to you.

```html
<!DOCTYPE html>
<html lang="en">
<head>
<meta charset="utf-8">
<title>Lumoveri.com Postcard</title>
<link rel="stylesheet" href="https://fonts.googleapis.com/css2?family=Arimo:wght@400;700&display=swap">
<style>
  :root {
    --brand-blue: #1d73dc;
    --brand-blue-dark: #0f5fc4;
    --headline-blue: #1a6cd4;
    --lime-light: #cfe64a;
    --lime-dark: #9dc41f;
    --ink: #1c1c1c;
    --white: #ffffff;
    --rule: #d9d9d9;
    --scene-light: #f4f6f7;
    --scene-mid: #dfe3e5;
  }
  * { margin: 0; padding: 0; box-sizing: border-box; }
  html, body {
    width: 1200px; height: 771px; overflow: hidden;
    background: var(--white);
    font-family: "Arimo", Arial, sans-serif;
  }
  .postcard { position: relative; width: 1200px; height: 771px; }

  .front-panel {
    position: absolute; left: 0; top: 0; width: 633px; height: 771px;
    overflow: hidden;
  }
  .interior-backdrop {
    position: absolute; inset: 0;
    background: linear-gradient(135deg, var(--scene-light) 0%, var(--scene-mid) 45%, #eef0f1 70%, #e3e6e8 100%);
  }
  .site-tab {
    position: absolute; left: 0; top: 0; width: 551px; height: 120px;
    background: linear-gradient(180deg, #2a86ea 0%, var(--brand-blue-dark) 100%);
    border-bottom-right-radius: 18px;
    display: flex; align-items: center; padding-left: 30px;
  }
  .site-name {
    color: var(--white); font-weight: 700; font-size: 56px; letter-spacing: 0.5px;
  }
  .tagline {
    position: absolute; left: 37px; top: 146px;
    color: var(--headline-blue); font-size: 31px; line-height: 34px; font-weight: 700;
  }
  .headline {
    position: absolute; left: 37px; top: 200px;
    color: var(--headline-blue); font-size: 31.5px; line-height: 31px; font-weight: 400;
  }
  .price-note {
    position: absolute; left: 305px; top: 372px; width: 310px;
    color: var(--headline-blue); font-size: 22px; line-height: 28px;
  }
  .price-note strong { font-weight: 700; }
  .price-footnote {
    display: block; margin-top: 6px;
    font-size: 15px; line-height: 18px; color: var(--ink);
  }
  .mom-photo {
    position: absolute; left: 0; top: 337px; width: 285px; height: 293px;
    background: radial-gradient(ellipse at 45% 45%, #c9a48c 0%, #6b4a38 45%, #2a2224 80%);
    border-top-right-radius: 40% 30%;
  }
  .produce-photo {
    position: absolute; left: 292px; top: 543px; width: 341px; height: 105px;
    background: linear-gradient(90deg, #d63a1e 0%, #c5221c 30%, #b3d34e 55%, #9cc33c 70%, #d0251a 90%);
    border-top-left-radius: 50px 60px;
    border-top-right-radius: 20px;
  }
  .forgive-tab {
    position: absolute; left: 0; top: 603px; width: 308px; height: 45px;
    background: linear-gradient(180deg, #2a86ea 0%, var(--brand-blue-dark) 100%);
    border-top-right-radius: 16px;
    color: var(--white); font-size: 25px; line-height: 45px; padding-left: 42px;
  }
  .promise-band {
    position: absolute; left: 0; top: 648px; width: 633px; height: 123px;
    background: linear-gradient(180deg, var(--lime-light) 0%, var(--lime-dark) 100%);
    padding: 14px 0 0 28px;
  }
  .promise-copy {
    color: var(--ink); font-size: 25px; line-height: 28px; letter-spacing: -0.2px;
  }
  .promise-copy sup { font-size: 14px; line-height: 0; vertical-align: 9px; }

  .stamp-box {
    position: absolute; left: 996px; top: 15px; width: 176px; height: 177px;
    border: 1.5px solid var(--rule);
  }
  .address-line {
    position: absolute; left: 683px; width: 466px; height: 0;
    border-top: 1.5px solid var(--rule);
  }
</style>
</head>
<body>
<div class="postcard">
  <section class="front-panel">
    <div class="interior-backdrop" role="img" aria-label="Soft-focus bright modern kitchen interior"></div>
    <header class="site-tab"><span class="site-name">lumoveri.example</span></header>
    <h1 class="tagline">Quiet Hurts — Healed.</h1>
    <p class="headline">Your health.<br>Your child’s reading skills.<br>You’re moments away from a fresh start!</p>
    <div class="mom-photo" role="img" aria-label="Smiling mother with long brown hair leaning in from the left"></div>
    <p class="price-note">For <strong>less than $10 a month*</strong>, Science can help you with either or both of these quiet hurts.<span class="price-footnote">*(annual subscription)</span></p>
    <div class="produce-photo" role="img" aria-label="Fresh tomato, red apple, green grapes and red bell pepper"></div>
    <div class="forgive-tab">Forgive yourself.</div>
    <div class="promise-band">
      <p class="promise-copy">Whether to help accelerate your child’s reading,<br>or to help YOU stick with your nutrition and activity<br>plans, Lumoveri<sup>TM</sup> science-based help is on the way!</p>
    </div>
  </section>

  <div class="stamp-box"></div>
  <div class="address-line" style="top:528px"></div>
  <div class="address-line" style="top:585px"></div>
  <div class="address-line" style="top:642px"></div>
  <div class="address-line" style="top:698px"></div>
</div>
</body>
</html>
```